new roofing company card

New primary business card for roofing company.

Industry/Entity Type

Residential roofing/Specializing in Asphalt and Standing seam metal roofing

Contact Information for Business Card

Phone number is: 555 471 2086 Email: support@halvenshingleworks.example website: www.halvenshingleworks.example

Colors
EB3D1F
EC4F4E
F09395
F8D3D4
FCEDEE

```html
<!DOCTYPE html>
<html lang="en">
<head>
<meta charset="utf-8">
<title>Halven Shingleworks – Business Card</title>
<link rel="stylesheet" href="https://fonts.googleapis.com/css2?family=Montserrat:wght@500;700&family=Open+Sans:wght@400;600&display=swap">
<style>
  :root {
    --page-bg: #2b2b2b;
    --card-dark: #262826;
    --card-white: #ffffff;
    --brand-red: #c0322a;
    --band-dark: #252725;
    --text-light: #ffffff;
    --wordmark-red: #c83a2c;
  }
  * { margin: 0; padding: 0; box-sizing: border-box; }
  html, body {
    width: 1200px; height: 977px; overflow: hidden;
    background: var(--page-bg);
  }
  .canvas { position: relative; width: 1200px; height: 977px; }

  .card {
    position: absolute;
    width: 560px; height: 320px;
    border-radius: 18px;
    overflow: hidden;
    box-shadow: 0 14px 30px rgba(0,0,0,.45);
  }

  /* Front side */
  .card-front {
    left: 70px; top: 120px;
    background: var(--card-dark);
    display: flex; align-items: center; justify-content: center;
  }
  .front-wordmark {
    display: flex; align-items: center; gap: 14px;
    font-family: "Montserrat", sans-serif;
    font-weight: 700;
    font-size: 34px;
    letter-spacing: .04em;
    color: var(--wordmark-red);
    text-transform: uppercase;
  }
  .mark-square { width: 22px; height: 22px; background: var(--wordmark-red); }

  /* Back side */
  .card-back {
    left: 570px; top: 537px;
    background: var(--card-white);
  }
  .back-band {
    position: absolute; left: 0; right: 0;
    top: 152px; height: 26px;
    background: var(--band-dark);
  }
  .back-red {
    position: absolute; left: 0; right: 0;
    top: 184px; bottom: 0;
    background: var(--brand-red);
  }
  .back-wordmark {
    position: absolute; left: 0; right: 0; top: 104px;
    display: flex; align-items: center; justify-content: center; gap: 10px;
    font-family: "Montserrat", sans-serif;
    font-weight: 700; font-size: 22px; letter-spacing: .04em;
    color: var(--wordmark-red);
    text-transform: uppercase;
  }
  .back-wordmark .mark-square { width: 16px; height: 16px; }

  .identity {
    position: absolute; left: 40px; top: 226px;
    width: 200px; text-align: right;
    color: var(--text-light);
  }
  .person-name {
    font-family: "Montserrat", sans-serif;
    font-weight: 700; font-size: 24px; letter-spacing: .01em;
    text-transform: uppercase; line-height: 1.1;
  }
  .person-role {
    font-family: "Open Sans", sans-serif;
    font-size: 14px; margin-top: 4px;
  }
  .divider {
    position: absolute; left: 258px; top: 212px;
    width: 1px; height: 82px;
    background: var(--text-light); opacity: .85;
  }
  .contacts {
    position: absolute; left: 276px; top: 214px;
    list-style: none;
    font-family: "Open Sans", sans-serif;
    font-size: 13px; color: var(--text-light);
  }
  .contacts li { display: flex; align-items: center; gap: 8px; height: 25px; }
  .contact-icon {
    width: 15px; height: 15px; flex: none;
    border-radius: 3px; background: var(--text-light);
    display: flex; align-items: center; justify-content: center;
  }
  .contact-icon svg { width: 11px; height: 11px; }
</style>
</head>
<body>
<main class="canvas">

  <section class="card card-front" aria-label="Card front">
    <div class="front-wordmark">
      <span class="mark-square"></span>
      <span>Halven Shingleworks</span>
    </div>
  </section>

  <section class="card card-back" aria-label="Card back">
    <div class="back-band"></div>
    <div class="back-red"></div>
    <div class="back-wordmark">
      <span class="mark-square"></span>
      <span>Halven Shingleworks</span>
    </div>

    <div class="identity">
      <p class="person-name">Daniel Mercer</p>
      <p class="person-role">Founder &amp; CEO</p>
    </div>
    <div class="divider"></div>

    <ul class="contacts">
      <li>
        <span class="contact-icon">
          <svg viewBox="0 0 24 24"><path fill="#c0322a" d="M6.6 10.8a15.1 15.1 0 0 0 6.6 6.6l2.2-2.2a1 1 0 0 1 1-.25 11.4 11.4 0 0 0 3.6.57 1 1 0 0 1 1 1V20a1 1 0 0 1-1 1A17 17 0 0 1 3 4a1 1 0 0 1 1-1h3.5a1 1 0 0 1 1 1c0 1.25.2 2.45.57 3.57a1 1 0 0 1-.25 1z"/></svg>
        </span>
        555 471 2086
      </li>
      <li>
        <span class="contact-icon">
          <svg viewBox="0 0 24 24"><path fill="#c0322a" d="M3 5h18v14H3z"/><path fill="none" stroke="#fff" stroke-width="2" d="M3 6l9 7 9-7"/></svg>
        </span>
        support@halvenshingleworks.example
      </li>
      <li>
        <span class="contact-icon">
          <svg viewBox="0 0 24 24"><circle cx="12" cy="12" r="9" fill="none" stroke="#c0322a" stroke-width="2.4"/><path fill="none" stroke="#c0322a" stroke-width="2" d="M3 12h18M12 3c3 3.5 3 14.5 0 18M12 3c-3 3.5-3 14.5 0 18"/></svg>
        </span>
        halvenshingleworks.example
      </li>
    </ul>
  </section>

</main>
</body>
</html>
```